Vessanta Company website for beauty pre & post natal products

i need to have a company website for my new start up company Vessanta. Vessanta means woman in latin. My website url is www.vessanta.com.sg, i have no contents yet. Vessanta is focus on selling pre and post natal beauty products e.g.: maternity belt, post natal girdles, maternity bra, etc.. products that beautify woman before and after maternity. I would like the website to potray beauty and yet confident woman. i have attached the sample of the product.
Updates

hi creative designers, I'm looking for your creativity that best to portray my company website, a local company based in Singapore that focus on selling beauty pre and post natal products to beautify motherhood and all women out there

Target Market(s)

Women (age 24-40), mother, career woman, etc

Industry/Entity Type

It Company

Number of Pages Required

5+ page

Font styles to use
Serif
Sans Serif

Requirements
Must have
• - Home page
• (highlights of products, company, beauty elegant women with small children, etc)
• - About Us
• Vessanta is founded in 2015 in Singapore by a proud mommy of 2 sons. During maternity period which before and after pregnancy, it is extremely crucial for woman to give extra care for herself and her body from the effect of pregnancy due to physical and hormonal changes.
• - Products
• - Client's testimonials
• - Contact Us
• - Inquiry Form
Nice to have
• Professional, yet elegant and appealing to women nowadays. It should show level of trust and credibility just from entering the website.
Should not have
• BIG NO to dark colors, gloomy colors or animations.

```html
<!DOCTYPE html>
<html lang="en">
<head>
<meta charset="utf-8">
<title>Vessanta</title>
<link rel="stylesheet" href="https://fonts.googleapis.com/css2?family=Noto+Serif:wght@400;700&display=swap">
<style>
:root{
  --brand-red:#820010;
  --brand-red-light:#c0283a;
  --title-red:#8a0f1c;
  --deep-maroon:#3a0006;
  --page-grey:#dedede;
  --white:#ffffff;
  --card-grey:#f3f3f3;
  --text-dark:#222222;
  --text-muted:#666666;
  --rule:#ececec;
}
*{margin:0;padding:0;box-sizing:border-box}
html,body{width:1200px;height:2198px;overflow:hidden}
body{position:relative;background:var(--page-grey);font-family:"Noto Serif",Georgia,serif;color:var(--text-dark)}
.abs{position:absolute}
.top-band{left:0;top:0;width:1200px;height:412px;background:var(--brand-red);border-top:5px solid var(--brand-red-light)}
.logo{left:100px;top:26px;font-size:38px;color:#f3c6c9;letter-spacing:1px;line-height:44px}
.nav{top:44px;font-size:14px;color:var(--white)}
.inquiry-btn{left:980px;top:36px;width:122px;height:32px;background:var(--deep-maroon);color:var(--white);font-size:14px;line-height:32px;text-align:center;border-radius:3px}
.hero{left:98px;top:110px;width:1002px;height:417px;background:var(--white)}
.hero-title{left:41px;top:160px;font-size:35px;line-height:44px;color:#333;white-space:nowrap;font-weight:400}
.hero-title b{font-weight:400;color:var(--title-red)}
.hero-btn{left:41px;top:274px;width:207px;height:55px;background:var(--deep-maroon);color:var(--white);font-size:19px;line-height:55px;text-align:center;border-radius:6px}
.dots{left:45px;top:378px;display:flex;gap:9px}
.dots span{width:10px;height:10px;border-radius:50%;background:#aaa}
.dots span.on{background:var(--deep-maroon)}
.hero-photo{left:692px;top:0;width:310px;height:417px;background:linear-gradient(180deg,#fbf4f3 0%,#e8c2c4 45%,#b8124a 75%,#f7eeee 100%)}
.content{left:98px;top:545px;width:1002px;height:769px;background:var(--white)}
.section-title{width:1002px;text-align:center;font-size:36px;color:var(--title-red);font-weight:400}
.rule{left:13px;width:977px;height:1px;background:var(--rule)}
.product-photo{top:91px;height:186px}
.product-label{top:290px;font-size:14px;text-align:center}
.card{top:460px;width:226px;height:277px;background:var(--card-grey)}
.card-photo{width:226px;height:168px}
.card-title{left:10px;top:180px;font-size:14px;color:var(--title-red)}
.card-desc{left:10px;top:200px;width:205px;font-size:11px;line-height:16px;color:var(--text-muted)}
.cart-btn{left:12px;top:237px;width:85px;height:27px;background:var(--brand-red);color:var(--white);font-size:11px;line-height:27px;text-align:center}
.testimonials{left:98px;top:1314px;width:1002px;height:514px;background:var(--brand-red);overflow:hidden}
.testimonial-photo{left:690px;top:0;width:312px;height:514px;background:linear-gradient(90deg,rgba(130,0,16,0) 0%,rgba(170,40,55,.7) 50%,rgba(120,0,15,.3) 100%)}
.t-title{top:48px;width:1002px;text-align:center;color:var(--white);font-size:36px;font-weight:400}
.avatar{left:432px;top:124px;width:138px;height:138px;border-radius:50%;background:linear-gradient(160deg,#e9d2cf,#b03040);border:4px solid #a94a54}
.t-name{top:282px;width:1002px;text-align:center;color:var(--white);font-size:20px}
.quote-mark{left:26px;top:300px;color:var(--white);font-size:48px;font-style:italic;line-height:48px}
.t-text{left:50px;top:344px;width:900px;text-align:center;color:var(--white);font-size:11.5px;line-height:20.5px}
.t-arrows{left:472px;top:456px}
.footer{left:98px;top:1828px;width:1002px;height:334px;background:var(--white)}
.f-head{top:60px;font-size:14px;color:var(--title-red);font-weight:400}
.f-text{top:104px;width:350px;font-size:11px;line-height:20.5px;color:#555}
.f-links{top:102px;font-size:11.5px;line-height:24px;color:#555;list-style:none}
.social{left:919px;width:28px;height:28px;border-radius:50%;background:#111}
.copyright{top:282px;width:1002px;text-align:center;font-size:11.5px;color:#444}
</style>
</head>
<body>
<div class="abs top-band"></div>
<div class="abs logo">Vessanta</div>
<nav>
  <div class="abs nav" style="left:526px">Home</div>
  <div class="abs nav" style="left:596px">About Us</div>
  <div class="abs nav" style="left:689px">Products</div>
  <div class="abs nav" style="left:778px">Testimonials</div>
  <div class="abs nav" style="left:891px">Contact Us</div>
  <div class="abs inquiry-btn">Inquiry Form</div>
</nav>

<section class="abs hero">
  <h1 class="abs hero-title"><b>Vessanta</b> is focus on selling pre and<br>post natal beauty products</h1>
  <div class="abs hero-btn">View Our Products</div>
  <div class="abs dots"><span class="on"></span><span></span><span></span><span></span></div>
  <div class="abs hero-photo" role="img" aria-label="Pregnant woman in a magenta top holding her belly"></div>
</section>

<section class="abs content">
  <h2 class="abs section-title" style="top:24px">Our Products</h2>
  <div class="abs rule" style="top:73px"></div>
  <div class="abs product-photo" style="left:13px;width:309px;background:linear-gradient(135deg,#f2e6da,#d9c2a6)" role="img" aria-label="Maternity belt worn around a pregnant belly"></div>
  <div class="abs product-photo" style="left:365px;width:270px;background:linear-gradient(135deg,#f4ece6,#d8b9a2)" role="img" aria-label="Woman wearing a beige post natal girdle"></div>
  <div class="abs product-photo" style="left:681px;width:309px;background:linear-gradient(135deg,#ecebe8,#c9b7a8)" role="img" aria-label="Woman in a maternity bra sitting by a window"></div>
  <div class="abs product-label" style="left:13px;width:309px">Maternity Belt</div>
  <div class="abs product-label" style="left:365px;width:270px">Post Natal Girdles</div>
  <div class="abs product-label" style="left:681px;width:309px">Maternity Bra</div>

  <h2 class="abs section-title" style="top:376px">Featured Product</h2>
  <div class="abs rule" style="top:435px"></div>

  <div class="abs card" style="left:13px">
    <div class="card-photo" style="background:linear-gradient(135deg,#555,#1c1c1c)" role="img" aria-label="Maternity bra in black and white"></div>
    <div class="abs card-title">Maternity Bra</div>
    <div class="abs card-desc">Neque porro quisquam est qui dolorem ipsum quia dolor sit amet</div>
    <div class="abs cart-btn">Add To Cart</div>
  </div>
  <div class="abs card" style="left:264px">
    <div class="card-photo" style="background:linear-gradient(180deg,#f6e4d8,#d9b49c 60%,#222 80%,#f0f0f0)" role="img" aria-label="Black support band on a pregnant belly"></div>
    <div class="abs card-title">Maternity Bra</div>
    <div class="abs card-desc">Neque porro quisquam est qui dolorem ipsum quia dolor sit amet</div>
    <div class="abs cart-btn">Add To Cart</div>
  </div>
  <div class="abs card" style="left:516px">
    <div class="card-photo" style="background:linear-gradient(90deg,#f4f4f4,#2a2a2a 45%,#1a1a1a 65%,#f2f2f2)" role="img" aria-label="Black shaping garment on a woman's waist"></div>
    <div class="abs card-title">Maternity Bra</div>
    <div class="abs card-desc">Neque porro quisquam est qui dolorem ipsum quia dolor sit amet</div>
    <div class="abs cart-btn">Add To Cart</div>
  </div>
  <div class="abs card" style="left:765px">
    <div class="card-photo" style="background:linear-gradient(90deg,#2a201b,#c99a7c 45%,#e9cdb8 60%,#2a201b)" role="img" aria-label="White maternity bra on a pregnant woman"></div>
    <div class="abs card-title">Maternity Bra</div>
    <div class="abs card-desc">Neque porro quisquam est qui dolorem ipsum quia dolor sit amet</div>
    <div class="abs cart-btn">Add To Cart</div>
  </div>
</section>

<section class="abs testimonials">
  <div class="abs testimonial-photo" role="img" aria-label="Red-toned photo of a woman in profile"></div>
  <h2 class="abs t-title">Testimonials</h2>
  <div class="abs avatar" role="img" aria-label="Customer portrait"></div>
  <div class="abs t-name">Dalia Marsh</div>
  <div class="abs quote-mark">&ldquo;</div>
  <p class="abs t-text">Lorem Ipsum is simply dummy text of the printing and typesetting industry. Lorem Ipsum has been the industry's standard dummy text ever since the 1500s, when an unknown printer took a galley of type and scrambled it to make a type specimen book. It has survived not only five centuries, but also the leap into electronic typesetting, remaining essentially unchanged. It was popularised in the 1960s with the release of Letterline sheets containing Lorem Ipsum passages, and more recently with desktop publishing software like Alder PageSetter including versions of Lorem Ipsum.</p>
  <svg class="abs t-arrows" width="58" height="24" viewBox="0 0 58 24">
    <circle cx="12" cy="12" r="10.5" fill="#fff"/>
    <path d="M14.5 7 L9.5 12 L14.5 17" stroke="#820010" stroke-width="2.6" fill="none" stroke-linecap="round" stroke-linejoin="round"/>
    <circle cx="46" cy="12" r="10.5" fill="#fff"/>
    <path d="M43.5 7 L48.5 12 L43.5 17" stroke="#820010" stroke-width="2.6" fill="none" stroke-linecap="round" stroke-linejoin="round"/>
  </svg>
</section>

<footer class="abs footer">
  <h3 class="abs f-head" style="left:13px">About Us</h3>
  <p class="abs f-text" style="left:13px">Vessanta is founded in 2015 in Singapore by a proud mommy of 2 sons. During maternity period which before and after pregnancy, it is extremely crucial for woman to give extra care for herself and her body from the effect of pregnancy due to physical and hormonal changes.</p>
  <h3 class="abs f-head" style="left:407px">Quick Links</h3>
  <ul class="abs f-links" style="left:407px"><li>Home</li><li>About Us</li><li>Products</li><li>Testimonials</li><li>Contact Us</li></ul>
  <h3 class="abs f-head" style="left:596px">Other Links</h3>
  <ul class="abs f-links" style="left:596px"><li>Privacy Policy</li><li>Terms &amp; Conditions</li></ul>
  <h3 class="abs f-head" style="left:765px">Connect With Us</h3>
  <ul class="abs f-links" style="left:765px;line-height:46px;top:92px"><li>Facelink</li><li>Chirper</li></ul>
  <div class="abs social" style="top:98px"></div>
  <div class="abs social" style="top:143px"></div>
  <div class="abs copyright">&copy; 2015 Company Name,All Right Reserved</div>
</footer>
</body>
</html>
```